Cloud Based Bookkeeping Website for Florists (Flower Shops)

We need a single page responsive website for a bookkeeping firm specializing in the floral industry. Our business model is based on the cloud and a goal is to attain floral clients from around the country, not only local.

Currently, we are attracted to flat illustration designs, but are concerned that they appear to informal or unprofessional. This webdesign should communicate professionalism, yet approachable, bright, attractive and modern.

The color scheme and overall design should match our designed logo, which is attached, and icon sets. We are open to new icon ideas and layout design, other than the layout we prepared and attached.

The attached layout we prepared has a holding place for a video at the top section. We own the video and can provide at a later time to insert. There is another secondary holding place for an explanation video, which we may or may not need, depending on the design your submit.

Lastly, I want to reiterate that we are open to new layout ideas.

Target Market(s)

Florists, Flower Shops

Industry/Entity Type

Bookkeeper

Number of Pages Required

2 page

Font styles to use
Sans Serif

Requirements
Must have
• Each section should be full width and screen height.
• Full page/section scrolling
• A price table
• A scrolling or fixed section displaying the third party app we work with.
• A blog page and a scrolling carousel displaying recent blog posts.
• Services section should be the six listed, but expandable to add more.
• A lead generation page, where clients can add attachments
• Must be a WordPress design so owner can easily modify and edit in the future
• Must be able to accommodate java script snippets in the header.
Nice to have
• A fixed "Contact Us" tab on the right side of the page that will lead to a contact form.

```html
<!DOCTYPE html>
<html lang="en">
<head>
<meta charset="utf-8">
<title>Bloomtally Bookkeeping</title>
<link rel="stylesheet" href="https://fonts.googleapis.com/css2?family=Source+Sans+3:wght@400;600;700&display=swap">
<style>
:root{
  --teal:#2fbfc4;
  --teal-dark:#22a9ae;
  --orange:#f26b36;
  --orange-light:#f58a4a;
  --ink:#2b2b2b;
  --text:#555;
  --muted:#888;
  --line:#e2e2e2;
  --soft:#f4f4f4;
  --white:#fff;
  --dark:#222;
}
*{box-sizing:border-box;margin:0;padding:0}
html,body{width:1200px;height:4286px;overflow:hidden}
body{font-family:"Source Sans 3",Arial,sans-serif;color:var(--text);background:var(--white);position:relative}
section,header,footer{position:absolute;left:0;width:1200px}
.abs{position:absolute}
.btn{position:absolute;display:flex;align-items:center;justify-content:center;background:var(--teal);color:var(--white);font-size:20px;font-weight:600;letter-spacing:.5px;text-transform:uppercase}
.section-title{position:absolute;left:0;width:1200px;text-align:center;font-size:42px;font-weight:400;color:var(--ink)}

/* nav */
.site-nav{top:0;height:86px;background:var(--white)}
.brand{position:absolute;display:flex;align-items:center;gap:12px}
.brand-mark{width:30px;height:30px;background:var(--orange)}
.brand-name{font-size:30px;font-weight:700;color:var(--teal)}
.nav-links{position:absolute;top:0;height:86px;display:flex;align-items:center;font-size:19px;color:var(--ink)}
.nav-links span{position:absolute;white-space:nowrap}
.nav-contact{position:absolute;right:0;top:0;width:182px;height:86px;background:var(--ink);color:var(--white);display:flex;align-items:center;justify-content:center;font-size:19px}

/* hero */
.hero{top:86px;height:591px}
.hero-photo{position:absolute;inset:0;background:linear-gradient(110deg,#d8dde0 0%,#b7c2c8 35%,#e9e3dc 60%,#cfd6da 100%)}
.hero-card{position:absolute;left:725px;top:151px;width:395px;height:271px;background:rgba(40,45,50,.78);padding:30px 24px}
.hero-card .brand-name{font-size:50px;color:var(--teal);line-height:1}
.hero-card h1{font-size:33px;font-weight:400;color:var(--white);line-height:1.25;margin-top:18px}

/* services */
.services{top:677px;height:717px}
.service{position:absolute;width:330px;text-align:center}
.service svg{display:block;margin:0 auto}
.service h3{font-size:22px;font-weight:600;color:var(--ink);margin-top:12px}
.service p{font-size:14px;line-height:1.45;margin-top:6px;color:var(--text)}

/* why */
.why{top:1394px;height:477px;background:linear-gradient(180deg,#f7f7f7,#fbf3f3)}
.why h2{position:absolute;left:77px;top:50px;font-size:44px;font-weight:400;color:var(--ink)}
.why h2 b{color:var(--teal);font-weight:600}
.why-copy{position:absolute;left:77px;top:120px;width:640px;font-size:14.5px;line-height:1.5}
.monitor{position:absolute;left:757px;top:34px;width:460px}
.monitor-screen{width:443px;height:268px;background:#1d1d1d;padding:12px}
.monitor-screen div{width:100%;height:100%;background:linear-gradient(180deg,#f5f5f5,#e8ecef)}
.monitor-stand{width:60px;height:22px;background:#cfd2d4;margin-left:190px}
.monitor-base{width:140px;height:8px;background:#bfc3c6;margin-left:150px;border-radius:3px}

/* how */
.how{top:1871px;height:529px;background:linear-gradient(120deg,var(--orange-light),var(--orange) 60%,#ee5a2a)}
.how .section-title{color:var(--white);top:50px}
.tablet{position:absolute;left:77px;top:120px;width:517px;height:380px;background:var(--white);border-radius:22px;padding:30px 44px}
.tablet-screen{width:100%;height:100%;background:linear-gradient(135deg,#cfd8cf,#f1e6e2 50%,#d9c9cf);position:relative}
.play{position:absolute;left:50%;top:50%;width:62px;height:62px;margin:-31px 0 0 -31px;border-radius:50%;background:var(--orange)}
.play:after{content:"";position:absolute;left:25px;top:19px;border-left:18px solid var(--white);border-top:12px solid transparent;border-bottom:12px solid transparent}
.how-copy{position:absolute;left:623px;top:120px;width:510px;color:var(--white);font-size:14.5px;line-height:1.55}

/* pricing */
.pricing{top:2400px;height:471px}
.plan{position:absolute;top:194px;width:329px;height:229px;border:1px solid var(--line);text-align:center}
.plan h3{font-size:22px;font-weight:400;color:var(--ink);margin-top:32px}
.price{font-size:44px;font-weight:700;color:var(--teal);margin-top:8px;line-height:1}
.price sup{font-size:20px;vertical-align:top;position:relative;top:4px}
.per{font-size:16px;color:var(--ink);margin-top:4px}
.plan .btn{left:114px;top:152px;width:100px;height:48px;font-size:18px}
.ribbon{position:absolute;left:434px;top:166px;width:329px;display:flex;justify-content:center}
.ribbon span{background:var(--orange);color:var(--white);font-size:17px;font-weight:700;padding:2px 20px}

/* blog */
.blog{top:2871px;height:386px;background:var(--soft)}
.post{position:absolute;top:118px;width:500px;height:254px;background:var(--white);border:1px solid var(--line)}
.post-photo{position:absolute;left:0;top:0;width:234px;height:100%}
.post-date{position:absolute;left:254px;top:0;width:60px;height:80px;background:var(--ink);color:var(--white);text-align:center;font-size:13px;padding-top:6px}
.post-date b{display:block;font-size:30px;line-height:1}
.post h3{position:absolute;left:254px;top:92px;width:230px;font-size:17px;font-weight:700;color:var(--ink);line-height:1.3}
.post p{position:absolute;left:254px;top:150px;width:230px;font-size:14px;line-height:1.45}
.post .more{position:absolute;right:16px;top:190px;font-size:14px;font-weight:600;color:var(--ink)}

/* lead */
.lead{top:3257px;height:557px}
.lead-bg{position:absolute;inset:0;background:linear-gradient(180deg,#3ec7cb,#69d2d4 60%,#7fd9da)}
.lead .section-title{color:var(--white);top:58px}
.lead-copy{position:absolute;top:120px;left:0;width:1200px;text-align:center;color:var(--white);font-size:16px;line-height:1.5}
.field{position:absolute;height:50px;border:1px solid rgba(255,255,255,.6);background:rgba(255,255,255,.15);color:var(--white);font-size:15px;padding:14px 14px}
.field.solid{background:var(--white);color:var(--ink)}
.dropzone{position:absolute;left:611px;top:252px;width:512px;height:177px;border:1px solid rgba(255,255,255,.6);background:rgba(255,255,255,.15);color:var(--white);font-size:22px;display:flex;align-items:center;justify-content:center;text-align:center;line-height:1.3}
.submit{position:absolute;left:537px;top:457px;width:126px;height:46px;background:var(--white);color:var(--teal);font-size:18px;font-weight:700;display:flex;align-items:center;justify-content:center}

/* partners */
.partners{top:3814px;height:143px;background:var(--white)}
.partner{position:absolute;top:52px;font-size:32px;font-weight:700;transform:translateX(-50%);white-space:nowrap}

/* footer */
.site-footer{top:3957px;height:266px;background:var(--teal);color:var(--white)}
.footer-brand{position:absolute;left:130px;top:80px;display:flex;align-items:center;gap:12px}
.footer-brand .brand-mark{background:var(--white)}
.footer-brand .brand-name{color:var(--white);font-size:28px}
.foot-col{position:absolute;top:42px}
.foot-col h4{font-size:21px;font-weight:600;margin-bottom:10px}
.foot-col li{list-style:none;font-size:15px;line-height:1.55}
.socials{display:flex;gap:18px}
.socials span{width:46px;height:46px;border-radius:50%;background:var(--dark)}
.contact-row{display:flex;align-items:center;gap:12px;font-size:15px;line-height:1;margin-bottom:14px}
.bottom-bar{top:4223px;height:63px;background:var(--dark);color:var(--white);font-size:14px}
.bottom-bar .left{position:absolute;left:77px;top:22px}
.bottom-bar .left b{color:var(--orange)}
.bottom-bar .right{position:absolute;right:77px;top:22px}
</style>
</head>
<body>

<header class="site-nav">
  <div class="brand" style="left:75px;top:26px"><span class="brand-mark"></span><span class="brand-name">Bloomtally</span></div>
  <nav class="nav-links">
    <span style="left:430px">My Account</span>
    <span style="left:560px">Remote Support</span>
    <span style="left:728px">Clients</span>
    <span style="left:820px">Blog</span>
  </nav>
  <div class="nav-contact">Contact</div>
</header>

<section class="hero">
  <div class="hero-photo" role="img" aria-label="Photo of two florists reviewing books on a tablet in a bright flower shop"></div>
  <div class="hero-card">
    <div class="brand-name">Bloomtally</div>
    <h1>Full Service Bookkeeping<br>for Florists</h1>
    <div class="btn" style="left:24px;top:198px;width:160px;height:52px;font-size:18px">Get Started</div>
  </div>
</section>

<section class="services">
  <h2 class="section-title" style="top:52px">What We Do?</h2>

  <div class="service" style="left:81px;top:166px">
    <svg width="60" height="60" viewBox="0 0 60 60" fill="none" stroke="#2fbfc4" stroke-width="2"><rect x="8" y="14" width="20" height="34"/><rect x="32" y="10" width="20" height="38"/><line x1="12" y1="24" x2="24" y2="24"/><line x1="36" y1="22" x2="48" y2="22"/></svg>
    <h3>Bookkeeping</h3>
    <p>If you send us a receipt, it'll be attached to its respective ledger transaction. Audit proofing your books is our goal.</p>
  </div>
  <div class="service" style="left:435px;top:166px">
    <svg width="60" height="60" viewBox="0 0 60 60" fill="none" stroke="#2fbfc4" stroke-width="2"><rect x="6" y="16" width="48" height="30"/><line x1="12" y1="38" x2="30" y2="38"/><line x1="38" y1="38" x2="50" y2="22"/></svg>
    <h3>Payroll</h3>
    <p>Paychecks &amp; payroll taxes guaranteed error-free. If there's ever an issue, we will represent you before the IRS.</p>
  </div>
  <div class="service" style="left:801px;top:166px">
    <svg width="60" height="60" viewBox="0 0 60 60" fill="none" stroke="#2fbfc4" stroke-width="2"><rect x="14" y="6" width="32" height="44"/><line x1="20" y1="20" x2="40" y2="20"/><line x1="20" y1="30" x2="40" y2="30"/><line x1="20" y1="40" x2="34" y2="40"/></svg>
    <h3>Sales Tax</h3>
    <p>We'll update tax rates when they change. Sales tax deposits and tax filings guaranteed error and penalty free.</p>
  </div>
  <div class="service" style="left:81px;top:397px">
    <svg width="60" height="60" viewBox="0 0 60 60" fill="none" stroke="#2fbfc4" stroke-width="2"><rect x="14" y="6" width="32" height="46"/><line x1="20" y1="18" x2="40" y2="18"/><line x1="20" y1="28" x2="40" y2="28"/><line x1="20" y1="38" x2="40" y2="38"/></svg>
    <h3>Financial Statements</h3>
    <p>Financial statements tell your story, let us help you make it a good one. With our metrics, you'll know where you can save money!</p>
  </div>
  <div class="service" style="left:435px;top:397px">
    <svg width="60" height="60" viewBox="0 0 60 60" fill="none" stroke="#2fbfc4" stroke-width="2"><circle cx="32" cy="20" r="10"/><path d="M6 44h14l10 6h18l6-8"/></svg>
    <h3>Accounts Payable</h3>
    <p>Send us your bills and invoices, we'll account for them and let you know when they are ready for your approval. You keep control of your bank accounts!</p>
  </div>
  <div class="service" style="left:801px;top:397px">
    <svg width="60" height="60" viewBox="0 0 60 60" fill="none" stroke="#2fbfc4" stroke-width="2"><path d="M8 24L30 10l22 14"/><line x1="8" y1="48" x2="52" y2="48"/><line x1="16" y1="28" x2="16" y2="44"/><line x1="30" y1="28" x2="30" y2="44"/><line x1="44" y1="28" x2="44" y2="44"/></svg>
    <h3>Reconciliations</h3>
    <p>One account or five, no worries – they're all included. We'll make sure that all of your expenses are accounted for.</p>
  </div>

  <div class="btn" style="left:505px;top:637px;width:190px;height:52px;font-size:18px">More Services</div>
</section>

<section class="why">
  <svg class="abs" style="left:0;top:0" width="1200" height="477" viewBox="0 0 1200 477"><path d="M560 477 C700 360 820 420 1200 300 L1200 477 Z" fill="#f7e6e6"/></svg>
  <h2>Why <b>Bloomtally</b></h2>
  <div class="why-copy">
    <p>We'll why not? You chose a path of a sole-proprietor and self-employment to make money, not waste it spending time sifting through receipts, processing invoices to pay your vendors, and preparing statements for your tax preparer. Your time can be better spent growing your business, not bookkeeping for your business.</p>
    <p>Although we can't proudly call ourselves designers, we've been in the floral industry for many years - washing buckets, cutting boxes, stocking shelves, delivering flowers, not to mention the sleepless holidays. Bookkeeping for a family flower shop started as a hobby, but transformed into an obsession. We understand the hard work and dedication that it takes to operate a successful flower shop and the profitability metrics every shop should strive to meet.</p>
  </div>
  <div class="btn" style="left:77px;top:370px;width:200px;height:52px;font-size:18px">Get Your Quote</div>
  <div class="btn" style="left:293px;top:370px;width:150px;height:52px;font-size:18px">Sign Up</div>
  <div class="monitor">
    <div class="monitor-screen"><div role="img" aria-label="Screenshot of an accounting dashboard with balance tables"></div></div>
    <div class="monitor-stand"></div>
    <div class="monitor-base"></div>
  </div>
</section>

<section class="how">
  <h2 class="section-title">Here's How It WorkS</h2>
  <div class="tablet">
    <div class="tablet-screen" role="img" aria-label="Video still of a florist arranging a bouquet"><span class="play"></span></div>
  </div>
  <div class="how-copy">
    <p>We tried hard to make this really simple!</p>
    <p>After joining our team, we'll send you a scanner and set it up for you. You simply scan your receipts, bills, &amp; invoices to us and we'll send you financial statements at the intervals you need them. Although we won't be printing and sending your bill payments, we'll send them to our payment processor where you'll log in and approve each bill – keeping you in full control of your bank accounts!</p>
    <p>Any opportunity we see to save you money, we'll reach out and let you know. It really is that simple!</p>
  </div>
  <div class="btn" style="left:623px;top:422px;width:206px;height:54px;font-size:18px">Get Your Quote</div>
  <div class="btn" style="left:843px;top:422px;width:146px;height:54px;font-size:18px">Sign Up</div>
</section>

<section class="pricing">
  <h2 class="section-title" style="top:90px">Our Prices are Very Competitive...</h2>
  <div class="ribbon"><span>MOST POPULAR</span></div>
  <div class="plan" style="left:77px">
    <h3>WEEKLY PLAN</h3>
    <div class="price">124<sup>96</sup></div>
    <div class="per">PER WEEK</div>
    <div class="btn">Enroll</div>
  </div>
  <div class="plan" style="left:434px">
    <h3>PAY IN FULL</h3>
    <div class="price">124<sup>96</sup></div>
    <div class="per">PER WEEK</div>
    <div class="btn">Enroll</div>
  </div>
  <div class="plan" style="left:791px">
    <h3>MONTHLY PLAN</h3>
    <div class="price">124<sup>96</sup></div>
    <div class="per">PER WEEK</div>
    <div class="btn">Enroll</div>
  </div>
</section>

<section class="blog">
  <h2 class="section-title" style="top:32px">Latest from Blog</h2>
  <article class="post" style="left:77px">
    <div class="post-photo" role="img" aria-label="Photo of a man in a shirt and tie at his desk" style="background:linear-gradient(135deg,#e4e4e4,#9a9a9a)"></div>
    <div class="post-date">DEC<b>15</b></div>
    <h3>LOREM IPSUM IS SIMPLY DUMMY</h3>
    <p>Lorem Ipsum is simply dummy text of the printing and typesetting industry.</p>
    <span class="more" style="color:var(--teal)">READ MORE</span>
  </article>
  <article class="post" style="left:620px">
    <div class="post-photo" role="img" aria-label="Photo of a ship's wooden steering wheel" style="background:linear-gradient(135deg,#7fa8c2,#8a5a3a)"></div>
    <div class="post-date">DEC<b>15</b></div>
    <h3>LOREM IPSUM IS SIMPLY DUMMY</h3>
    <p>Lorem Ipsum is simply dummy text of the printing and typesetting industry.</p>
    <span class="more">READ MORE</span>
  </article>
</section>

<section class="lead">
  <div class="lead-bg" role="img" aria-label="Teal-tinted photo of an office desk with paperwork"></div>
  <h2 class="section-title">Still Not Convinced?</h2>
  <div class="lead-copy">
    Then we can only assume that you're not lying underneath a pile of receipts!<br>
    No worries, we can still be friends! – Let us create a free wire service profitability report for you.<br>
    That's right FREE, this one is on us.
  </div>
  <div class="field solid" style="left:77px;top:252px;width:252px">Your Name:</div>
  <div class="field" style="left:337px;top:252px;width:252px">Shop Name:</div>
  <div class="field" style="left:77px;top:314px;width:252px">Email Address:</div>
  <div class="field" style="left:337px;top:314px;width:252px">Phone No.</div>
  <div class="field" style="left:77px;top:377px;width:512px">Website Address:</div>
  <div class="dropzone">Drag and drop your<br>statement here</div>
  <div class="submit">SUBMIT</div>
</section>

<section class="partners">
  <span class="partner" style="left:200px;color:#2ca01c">Ledgerly</span>
  <span class="partner" style="left:430px;color:#f26b1d">Payvault</span>
  <span class="partner" style="left:730px;color:#1e3a5a">Docstack</span>
  <span class="partner" style="left:1000px;color:#1f8fd6">Shiftwell</span>
</section>

<footer class="site-footer">
  <div class="footer-brand"><span class="brand-mark"></span><span class="brand-name">Bloomtally</span></div>
  <div class="foot-col" style="left:343px">
    <h4>Useful Links</h4>
    <ul><li>Home</li><li>About</li><li>Services</li><li>Client</li><li>Support</li><li>Blog</li></ul>
  </div>
  <div class="foot-col" style="left:560px">
    <h4>Follow Us On</h4>
    <div class="socials"><span aria-label="Social profile 1"></span><span aria-label="Social profile 2"></span><span aria-label="Social profile 3"></span></div>
  </div>
  <div class="foot-col" style="left:871px">
    <h4>Get In Touch With Us</h4>
    <div class="contact-row"><svg width="18" height="18" viewBox="0 0 24 24" fill="#fff"><path d="M6.6 10.8a15 15 0 006.6 6.6l2.2-2.2a1 1 0 011-.25 11.4 11.4 0 003.6.57 1 1 0 011 1V20a1 1 0 01-1 1A17 17 0 013 4a1 1 0 011-1h3.5a1 1 0 011 1c0 1.25.2 2.45.57 3.6a1 1 0 01-.25 1z"/></svg>123 456 7890</div>
    <div class="contact-row"><svg width="18" height="18" viewBox="0 0 24 24" fill="#fff"><path d="M6.6 10.8a15 15 0 006.6 6.6l2.2-2.2a1 1 0 011-.25 11.4 11.4 0 003.6.57 1 1 0 011 1V20a1 1 0 01-1 1A17 17 0 013 4a1 1 0 011-1h3.5a1 1 0 011 1c0 1.25.2 2.45.57 3.6a1 1 0 01-.25 1z"/></svg>123 456 7890</div>
    <div class="contact-row"><svg width="18" height="18" viewBox="0 0 24 24" fill="none" stroke="#fff" stroke-width="2"><rect x="3" y="5" width="18" height="14"/><path d="M3 6l9 7 9-7"/></svg>info@bloomtally.com</div>
  </div>
</footer>

<div class="bottom-bar" style="position:absolute;left:0;width:1200px">
  <span class="left">© <b>Bloomtally</b> - 2017. All Rights Reserved.</span>
  <span class="right">Privacy Policy</span>
</div>

</body>
</html>
```